Mesh Banner Design for Business Premises

We require the design of a large mesh banner to be installed across the front fence of our warehouse. The banner should prominently feature our existing Trelborn logo and brand colours (yellow, white, and black) and be designed to be highly visible from the road.

The overall aesthetic should be strong, masculine, and industrial, reflecting the nature of the scaffolding and construction industry. The background should be predominantly black, with our branding incorporated in yellow and white for strong contrast and readability.

The banner should clearly communicate the full scope of services we provide, including:

Scaffold Design
Scaffold Engineering
Scaffold Installation / Erection
Scaffold Dismantling

It should also indicate the types of projects and clients we service, including:

Commercial
Industrial
Residential
Civil

The design should feel bold and professional, with a construction-oriented style that aligns with the scaffolding industry. It should be clean, impactful, and easy to read from a distance, ensuring passing traffic can quickly understand our services.

Where possible, subtle industrial or structural design elements (such as scaffold components, steel textures, or linework) may be incorporated into the background to reinforce the industry theme while keeping the layout uncluttered.

The final design will be produced as a large-format mesh banner for outdoor installation, so it should be created with this application and viewing distance in mind.

```html
<!DOCTYPE html>
<html lang="en">
<head>
<meta charset="utf-8">
<title>Trelborn – Warehouse Fence Banner</title>
<link href="https://fonts.googleapis.com/css2?family=Roboto+Condensed:wght@700&family=Questrial&display=swap" rel="stylesheet">
<style>
  :root {
    --page: #ffffff;
    --banner-black: #1d1d1f;
    --band-grey: #3a3a3c;
    --brand-yellow: #f5a21c;
    --brand-white: #ffffff;
  }
  * { margin: 0; padding: 0; box-sizing: border-box; }
  html, body { width: 862px; height: 1200px; overflow: hidden; background: var(--page); }
  .canvas { position: relative; width: 862px; height: 1200px; }
  .banner {
    position: absolute; left: 0; top: 320px; width: 862px; height: 560px;
    background: var(--banner-black); overflow: hidden;
    font-family: "Roboto Condensed", "Arial Narrow", sans-serif;
  }
  .site-backdrop {
    position: absolute; inset: 0;
    background:
      radial-gradient(ellipse at 55% 55%, rgba(90,70,50,0.28), transparent 60%),
      linear-gradient(180deg, rgba(40,40,44,0) 0%, rgba(55,50,46,0.35) 60%, rgba(30,30,32,0.2) 100%);
  }
  .linework { position: absolute; inset: 0; }
  .brand { position: absolute; left: 71px; top: 58px; display: flex; align-items: center; }
  .brand-square { width: 44px; height: 44px; background: var(--brand-yellow); margin-right: 154px; }
  .brand-name {
    color: var(--brand-white); font-size: 44px; font-weight: 700;
    letter-spacing: 27px; line-height: 1;
  }
  .section-title {
    position: absolute; top: 174px; height: 43px; line-height: 43px;
    color: var(--brand-yellow); font-size: 25px; font-weight: 700; text-align: center;
  }
  .section-title.services { left: 124px; width: 290px; }
  .section-title.projects { left: 540px; width: 300px; }
  .list { position: absolute; list-style: none; color: var(--brand-white); font-size: 22px; font-weight: 700; }
  .list li { height: 41.5px; line-height: 20px; display: flex; align-items: flex-start; }
  .list li svg { width: 14px; height: 14px; margin: 3px 9px 0 0; flex: none; }
  .list.services { left: 137px; top: 236px; }
  .list.projects { left: 592px; top: 236px; }
  .phone {
    position: absolute; left: 0; width: 862px; top: 415px; text-align: center;
    font-family: "Questrial", "Century Gothic", sans-serif; color: var(--brand-white);
    font-size: 76px; line-height: 1;
  }
  .call-to-action {
    position: absolute; left: 0; width: 862px; top: 512px; text-align: center;
    color: var(--brand-yellow); font-size: 24px; font-weight: 700;
  }
</style>
</head>
<body>
<div class="canvas">
  <section class="banner">
    <div class="site-backdrop" role="img" aria-label="Faint construction site backdrop with tower crane and building frames"></div>

    <svg class="linework" viewBox="0 0 862 560" aria-hidden="true">
      <defs>
        <linearGradient id="streak-left" x1="0" x2="1">
          <stop offset="0" stop-color="#f5a21c"/><stop offset="1" stop-color="#f5a21c" stop-opacity="0"/>
        </linearGradient>
        <linearGradient id="streak-right" x1="1" x2="0">
          <stop offset="0" stop-color="#f5a21c"/><stop offset="1" stop-color="#f5a21c" stop-opacity="0"/>
        </linearGradient>
      </defs>
      <g fill="var(--band-grey)">
        <polygon points="140,174 408,174 433,217 134,217 121,203"/>
        <polygon points="558,174 862,174 862,217 529,217"/>
      </g>
      <g fill="none" stroke="var(--brand-yellow)" stroke-width="2.2">
        <polyline points="0,203 121,203 140,174 408,174 433,217 548,402"/>
        <line x1="134" y1="217" x2="433" y2="217"/>
        <line x1="121" y1="203" x2="0" y2="377"/>
        <line x1="57" y1="297" x2="121" y2="402"/>
        <polyline points="862,174 558,174 529,217 480,287"/>
        <line x1="529" y1="217" x2="862" y2="217"/>
        <line x1="0" y1="402" x2="862" y2="402"/>
      </g>
      <g>
        <rect x="0" y="437" width="260" height="6" fill="url(#streak-left)"/>
        <rect x="0" y="461" width="180" height="5" fill="url(#streak-left)" opacity="0.8"/>
        <rect x="0" y="485" width="240" height="6" fill="url(#streak-left)"/>
        <rect x="602" y="437" width="260" height="6" fill="url(#streak-right)"/>
        <rect x="682" y="461" width="180" height="5" fill="url(#streak-right)" opacity="0.8"/>
        <rect x="622" y="485" width="240" height="6" fill="url(#streak-right)"/>
      </g>
    </svg>

    <div class="brand">
      <span class="brand-square"></span>
      <span class="brand-name">TRELBORN</span>
    </div>

    <h2 class="section-title services">CORE SERVICES</h2>
    <h2 class="section-title projects">PROJECT TYPES</h2>

    <ul class="list services">
      <li><svg viewBox="0 0 14 14"><path d="M1 2l5 5-5 5M7 2l5 5-5 5" fill="none" stroke="#f5a21c" stroke-width="2"/></svg>Scaffold Design</li>
      <li><svg viewBox="0 0 14 14"><path d="M1 2l5 5-5 5M7 2l5 5-5 5" fill="none" stroke="#f5a21c" stroke-width="2"/></svg>Scaffold Engineering</li>
      <li><svg viewBox="0 0 14 14"><path d="M1 2l5 5-5 5M7 2l5 5-5 5" fill="none" stroke="#f5a21c" stroke-width="2"/></svg>Scaffold Installation / Erection</li>
      <li><svg viewBox="0 0 14 14"><path d="M1 2l5 5-5 5M7 2l5 5-5 5" fill="none" stroke="#f5a21c" stroke-width="2"/></svg>Scaffold Dismantling</li>
    </ul>
    <ul class="list projects">
      <li><svg viewBox="0 0 14 14"><path d="M1 2l5 5-5 5M7 2l5 5-5 5" fill="none" stroke="#f5a21c" stroke-width="2"/></svg>Commercial</li>
      <li><svg viewBox="0 0 14 14"><path d="M1 2l5 5-5 5M7 2l5 5-5 5" fill="none" stroke="#f5a21c" stroke-width="2"/></svg>Industrial</li>
      <li><svg viewBox="0 0 14 14"><path d="M1 2l5 5-5 5M7 2l5 5-5 5" fill="none" stroke="#f5a21c" stroke-width="2"/></svg>Residential</li>
      <li><svg viewBox="0 0 14 14"><path d="M1 2l5 5-5 5M7 2l5 5-5 5" fill="none" stroke="#f5a21c" stroke-width="2"/></svg>Civil</li>
    </ul>

    <p class="phone">1300 8 BUILD</p>
    <p class="call-to-action">CALL NOW FOR SCAFFOLD SOLUTIONS</p>
  </section>
</div>
</body>
</html>
```